Zielgruppe
Wir sind KQ Rapid Voltwerk GmbH mit Sitz in Basel Schweiz. Wir bieten die volle Palette von Elektronikdienstleistungen. Besonders aber Photovoltaik (Solar) auf Einfamilienhäusern und Gewerbeeinheiten, Smart Home Automation mit Dravix (Partner) und allgemeine Elektrikerdienstleistungen in Häusern und Wohnung.
USP
• Regionale Firma, BS, BL,AG
○ Daher schnelle Reaktion im Störungsfall. Garantierte Entstörung
• Umsetzung innert 2-3 Monate
• Planung und Durchführung aus einer Hand.
• Umsetzung auch in der PV Installation nur durch eigene Mitarbeiter
• Kelmora Förderung, bis zu 6TCHF
• Kompetent, freundlich
• Eidgenössich diplomierter Elektroinstallateur (Meister)
• EFZ (Eidgenösisch Fährigkeitszeugnis)
• 1 Jahr Existenz
• Dravix goldpartner
• Nur Doppelglasmodule mit 25 Jahre Garantie, 10 Jahre auf Wechselrichter und Batterie
• Planung mittels CAD/*D Planung, technische Tool
• Genaues und schnelles Angebot innert 5 Werktagen
USP:
• Stromkosten sparen
• Autark werden, unabhängig von Strompreisentwicklung
• Umwelt schützen
WUNSCHKUNDE
• Soziodemografisch
○ Eigentümer
○ Gehobene Mittelklasse
• Lokalität in Basel und Umgebung
Aufgabenstellung
Medien unter: https://files.trobelix.ch/index.php/s/mQzWnLpRtYvA7KD
Logo ist dort vorhanden.
Hintergrund hell (weiss, hellgrau bspw.)
Schriftart
Verlinkungen zu Social Media:
• Facebook
• Linkedin
• Instagram
Beispielseiten, die gefallen:
Alpin Lichtfeld Werk (alpin-lichtfeld-werk.ch) Prio
Counter mit

```html
<!DOCTYPE html>
<html lang="de">
<head>
<meta charset="utf-8">
<title>KQ Rapid Voltwerk – Solaranfrage</title>
<link href="https://fonts.googleapis.com/css2?family=Poppins:wght@800&family=Catamaran:wght@400;500&family=Inter:wght@400;600;700&display=swap" rel="stylesheet">
<style>
:root{
  --title:#7a8b9b;
  --text:#555f69;
  --green:#0b7a1c;
  --ink:#111;
  --line:#8a96a2;
  --bg:#ffffff;
}
*{box-sizing:border-box;margin:0;padding:0}
html,body{width:1200px;height:3681px;overflow:hidden;background:var(--bg)}
body{position:relative;font-family:"Catamaran",sans-serif;color:var(--text)}
.step-title{position:absolute;left:0;width:1200px;text-align:center;font-family:"Poppins",sans-serif;font-weight:800;font-size:42px;line-height:45px;color:var(--title);letter-spacing:-.3px}
.icon{position:absolute;border-radius:14px}
.option{position:absolute;display:flex;align-items:center;gap:8px;font-size:17px;color:var(--text);transform:translateY(-50%);white-space:nowrap}
.option.center{left:0;width:1200px;justify-content:center}
.radio{width:15px;height:15px;border:1.5px solid #4d5661;border-radius:50%;display:inline-flex;align-items:center;justify-content:center}
.radio.on{border-color:var(--green)}
.radio.on::after{content:"";width:7px;height:7px;border-radius:50%;background:var(--green)}
.btn{position:absolute;background:var(--green);color:#fff;font-family:"Inter",sans-serif;font-weight:600;font-size:19px;display:flex;align-items:center;justify-content:center;border-radius:3px;box-shadow:0 3px 4px rgba(0,0,0,.25)}
.next{left:561px;width:99px;height:40px}
.final-title{top:2850px}
.lead{position:absolute;left:169px;top:2922px;width:420px;font-family:"Poppins",sans-serif;font-weight:800;font-size:25px;line-height:34px;color:var(--title);letter-spacing:-.2px}
.copy{position:absolute;left:169px;width:430px;font-family:"Inter",sans-serif;font-size:12.5px;line-height:18px;color:#222}
.copy strong{font-weight:700;color:var(--ink)}
.contact{position:absolute;left:185px;display:flex;align-items:center;gap:14px;font-family:"Poppins",sans-serif;font-weight:800;font-size:23px;color:var(--green);line-height:40px}
.contact .dot{width:40px;height:40px;border-radius:50%;background:var(--green);display:flex;align-items:center;justify-content:center}
.label{position:absolute;left:643px;font-family:"Inter",sans-serif;font-weight:700;font-size:11px;color:#4a525a}
.field{position:absolute;left:639px;width:392px;height:44px;border:1px solid var(--line);border-radius:4px;background:#fff}
.note{position:absolute;left:54px;top:3452px;width:320px;font-family:"Inter",sans-serif;font-size:14px;line-height:16.5px;color:var(--ink)}
</style>
</head>
<body>

<!-- Schritt 1 -->
<h2 class="step-title" style="top:80px">Wie möchten Sie Ihren selbst<br>erzeugten Strom nutzen?</h2>
<div class="icon" role="img" aria-label="Illustration Solarmodule mit Sonne" style="left:436px;top:209px;width:94px;height:94px;background:linear-gradient(160deg,#fde7a3,#cfd8df 60%,#9fb3c2)"></div>
<div class="option" style="left:555px;top:253px"><span class="radio on"></span>Eigenverbrauch ohne Speicher</div>
<div class="icon" role="img" aria-label="Illustration Solaranlage mit Batteriespeicher" style="left:436px;top:329px;width:94px;height:94px;background:linear-gradient(160deg,#fde7a3,#7fa2d6 55%,#3c6db3)"></div>
<div class="option" style="left:555px;top:373px"><span class="radio"></span>Eigenverbrauch mit Speicher</div>
<div class="icon" role="img" aria-label="Illustration Fragezeichen" style="left:436px;top:450px;width:94px;height:94px;background:linear-gradient(120deg,#f5c24a,#3a7fd0 55%,#58c59a)"></div>
<div class="option" style="left:555px;top:494px"><span class="radio"></span>Noch nicht entschieden</div>
<div class="btn next" style="top:579px">Weiter</div>

<!-- Schritt 2 -->
<h2 class="step-title" style="top:752px">An welche Eigentumsfläche ist<br>die PV-Anlage zu installieren?</h2>
<div class="icon" role="img" aria-label="Illustration privates Einfamilienhaus" style="left:418px;top:882px;width:94px;height:90px;background:linear-gradient(160deg,#f08aa0,#f6e8c8 55%,#8cc46a)"></div>
<div class="option" style="left:540px;top:926px"><span class="radio on"></span>Privates Eigenheim</div>
<div class="icon" role="img" aria-label="Illustration Gewerbegebäude" style="left:416px;top:998px;width:104px;height:96px;background:linear-gradient(160deg,#b9d3ee,#7ea7d8 55%,#8cc46a)"></div>
<div class="option" style="left:540px;top:1047px"><span class="radio"></span>Gewerbe-Immobilie/Industrie</div>
<div class="btn next" style="top:1130px">Weiter</div>

<!-- Schritt 3 -->
<h2 class="step-title" style="top:1303px">Wie viel kWh haben Sie in Ihrer<br>letzten Abrechnung verbraucht?</h2>
<div class="icon" role="img" aria-label="Illustration Stecker mit Blitz" style="left:563px;top:1434px;width:84px;height:90px;background:linear-gradient(160deg,#efe3c0,#5f93d6 60%,#2f5e9e)"></div>
<div class="option center" style="top:1567px"><span class="radio on"></span>1.000 - 2.500 kWh</div>
<div class="option center" style="top:1639px"><span class="radio"></span>2.500 - 5.000 kWh</div>
<div class="option center" style="top:1711px"><span class="radio"></span>5.000 - 7.500 kWh</div>
<div class="option center" style="top:1783px"><span class="radio"></span>7.500 - 10.000 kWh</div>
<div class="option center" style="top:1855px"><span class="radio"></span>Mehr als 10.000 kWh</div>
<div class="btn next" style="top:1905px">Weiter</div>

<!-- Schritt 4 -->
<h2 class="step-title" style="top:2081px">An welche Fläche soll Ihre<br>PV-Anlage errichtet werden?</h2>
<div class="icon" role="img" aria-label="Illustration Haus mit Solardach" style="left:461px;top:2200px;width:94px;height:96px;background:linear-gradient(160deg,#fde7a3,#e6c98f 55%,#8aa3b8)"></div>
<div class="option" style="left:590px;top:2252px"><span class="radio on"></span>Dach</div>
<div class="icon" role="img" aria-label="Illustration Solarüberdachung" style="left:461px;top:2325px;width:94px;height:94px;background:linear-gradient(160deg,#fde7a3,#8fb8e2 55%,#3e6ea8)"></div>
<div class="option" style="left:590px;top:2373px"><span class="radio"></span>Überdachung</div>
<div class="icon" role="img" aria-label="Illustration Solarpark auf Freifläche" style="left:461px;top:2445px;width:94px;height:94px;background:linear-gradient(160deg,#f6c143,#8fc0ea 55%,#7fbf5f)"></div>
<div class="option" style="left:590px;top:2493px"><span class="radio"></span>Freifläche</div>
<div class="icon" role="img" aria-label="Illustration Solarmodul an Fassade" style="left:470px;top:2566px;width:80px;height:94px;background:linear-gradient(160deg,#fde7a3,#4f7fc4 55%,#f3c34a)"></div>
<div class="option" style="left:590px;top:2614px"><span class="radio"></span>Fassadenbauteile</div>
<div class="btn next" style="top:2697px">Weiter</div>

<!-- Abschluss -->
<h2 class="step-title final-title">Gleich geschafft!</h2>
<p class="lead">Wir freuen uns, Ihnen ein Angebot machen zu dürfen!</p>
<p class="copy" style="top:3012px"><strong>Versprochen - 100% unverbindlich, 100% kostenlos!</strong></p>
<p class="copy" style="top:3051px">Bitte geben Sie Ihre Kontaktdaten im Formular an, damit wir Ihnen unser Angebot übermitteln können!</p>
<p class="copy" style="top:3107px">Bei Anliegen, Anfragen oder für eine persönliche Beratung stehen wir Ihnen gerne zur Verfügung. Hier finden Sie unsere Kontaktdaten für einen direkten Draht zu unserem Team.</p>
<div class="contact" style="top:3181px">
  <span class="dot"><svg width="20" height="20" viewBox="0 0 24 24"><path fill="#fff" d="M6.6 10.8a15.1 15.1 0 0 0 6.6 6.6l2.2-2.2a1 1 0 0 1 1-.25 11.4 11.4 0 0 0 3.6.57 1 1 0 0 1 1 1V20a1 1 0 0 1-1 1A17 17 0 0 1 3 4a1 1 0 0 1 1-1h3.5a1 1 0 0 1 1 1c0 1.25.2 2.45.57 3.57a1 1 0 0 1-.25 1z"/></svg></span>+49 170 555 28 14
</div>
<div class="contact" style="top:3231px">
  <span class="dot"><svg width="20" height="20" viewBox="0 0 24 24"><path fill="#fff" d="M3 6h18v12H3z"/><path fill="none" stroke="#0b7a1c" stroke-width="2" d="M3 6l9 7 9-7"/></svg></span>info@kqvoltwerk.de
</div>

<form>
  <span class="label" style="top:2958px">Name*</span>
  <div class="field" style="top:2981px"></div>
  <span class="label" style="top:3037px">Telefonnummer</span>
  <div class="field" style="top:3059px"></div>
  <span class="label" style="top:3114px">E-Mail-Adresse*</span>
  <div class="field" style="top:3137px"></div>
  <div class="btn" style="left:771px;top:3200px;width:131px;height:38px">Absenden</div>
</form>

<p class="note">Notiz: Auf Mobile den letzten Schritt anders anordnen, die zwei Spalten werden zu einer: Direkt nach “Bitte geben Sie Ihre Kontaktdaten im Formular an, damit wir Ihnen unser Angebot übermitteln können!” kommt das Formular, darunter der Absatz “Bei Anliegen, Anfragen oder für eine persönliche Beratung stehen wir Ihnen gerne zur Verfügung. Hier finden Sie unsere Kontaktdaten für einen direkten Draht zu unserem Team.”</p>

</body>
</html>
```